Looking for a creative label design for our retail coffee bags

We are a coffee manufacturer (coffee roaster) looking to re-brand our retail label for our coffee bags. Our main coffee blend that we sell is our Harborline Velvet Blend. You can use this name when creating the label. We are going for a look that represents our company as a coffee roaster. Please reference our website (www.brindlemugworks.com) and our Facebook page to learn more about our company and to give you more inspiration on creating this design.

Target Market(s)

Retail customers/grocery stores

Industry/Entity Type

Manufacturer

Requirements
Must have
• The size of the label has to be 3" width x 4" height

Logo must be Black
Nice to have
• We currently incorporate a color on our labels for each blend. For example, Harborline Velvet Blend (royal blue), Decaffeinated Blend (red), Breakfast Blend (green), Flavored coffees (gold).

Rustic/vintage style

```html
<!DOCTYPE html>
<html lang="en">
<head>
<meta charset="utf-8">
<title>Harborline Velvet Blend – Retail Label</title>
<link rel="stylesheet" href="https://fonts.googleapis.com/css2?family=Alfa+Slab+One&family=Josefin+Sans:wght@600&family=Playfair+Display:wght@400&display=swap">
<style>
  :root {
    --page: #ececec;
    --label-border: #f8e8c6;
    --navy: #344a66;
    --navy-deep: #2c3f58;
    --stripe: rgba(212, 206, 168, 0.75);
    --frame: #c9c9a4;
    --ink: #121212;
    --cream: #f5ecd6;
    --bean-tone: #9a917c;
    --roast: #241f1c;
    --white: #ffffff;
  }
  * { margin: 0; padding: 0; box-sizing: border-box; }
  html, body {
    width: 1200px;
    height: 1173px;
    overflow: hidden;
    background: var(--page);
  }
  .label {
    position: absolute;
    left: 175px;
    top: 55px;
    width: 850px;
    height: 1062px;
    background: var(--label-border);
    box-shadow: 0 18px 40px rgba(0,0,0,0.12);
  }
  .label-face {
    position: absolute;
    left: 33px;
    top: 33px;
    width: 778px;
    height: 995px;
    background-color: var(--navy);
    background-image: repeating-linear-gradient(
      90deg,
      transparent 0 22px,
      var(--stripe) 22px 24px
    );
    overflow: hidden;
  }
  .label-art { position: absolute; inset: 0; }
  .blend-title {
    font-family: "Alfa Slab One", serif;
    fill: var(--white);
    stroke: var(--ink);
    stroke-width: 4;
    paint-order: stroke;
  }
  .blend-title-shadow {
    font-family: "Alfa Slab One", serif;
    fill: var(--ink);
  }
  .tagline {
    font-family: "Josefin Sans", sans-serif;
    font-weight: 600;
    fill: var(--cream);
    letter-spacing: 4px;
  }
  .brand-name {
    font-family: "Josefin Sans", sans-serif;
    font-weight: 600;
    fill: var(--cream);
  }
  .net-weight {
    font-family: "Playfair Display", serif;
    fill: var(--cream);
  }
</style>
</head>
<body>
  <div class="label">
    <div class="label-face">
      <svg class="label-art" viewBox="0 0 778 995" width="778" height="995" xmlns="http://www.w3.org/2000/svg">
        <!-- shield frame -->
        <polygon class="shield-fill" points="136,166 640,166 640,683 389,738 136,683" fill="var(--navy)"/>
        <polygon class="shield-frame" points="136,166 640,166 640,683 389,738 136,683" fill="none" stroke="var(--frame)" stroke-width="11" stroke-linejoin="miter"/>

        <!-- brand mark -->
        <g class="brand-badge">
          <circle cx="389" cy="161" r="112" fill="var(--ink)"/>
          <text class="brand-name" x="389" y="155" text-anchor="middle" font-size="30">BRINDLE</text>
          <text class="brand-name" x="389" y="192" text-anchor="middle" font-size="30">MUGWORKS</text>
        </g>

        <!-- blend name -->
        <text class="blend-title-shadow" x="395" y="471" text-anchor="middle" font-size="150" textLength="605" lengthAdjust="spacingAndGlyphs">HARBORLINE</text>
        <text class="blend-title" x="389" y="465" text-anchor="middle" font-size="150" textLength="605" lengthAdjust="spacingAndGlyphs">HARBORLINE</text>
        <text class="blend-title-shadow" x="392" y="563" text-anchor="middle" font-size="70" textLength="437" lengthAdjust="spacingAndGlyphs">VELVET BLEND</text>
        <text class="blend-title" x="389" y="560" text-anchor="middle" font-size="70" textLength="437" lengthAdjust="spacingAndGlyphs" stroke-width="3">VELVET BLEND</text>

        <!-- coffee cup icon -->
        <g class="cup-icon" fill="var(--frame)">
          <path d="M376 592 q-6 -8 0 -16 q6 -8 0 -16" fill="none" stroke="var(--frame)" stroke-width="3"/>
          <path d="M389 592 q-6 -8 0 -16 q6 -8 0 -16" fill="none" stroke="var(--frame)" stroke-width="3"/>
          <path d="M402 592 q-6 -8 0 -16 q6 -8 0 -16" fill="none" stroke="var(--frame)" stroke-width="3"/>
          <path d="M366 600 h46 v6 q0 22 -23 22 q-23 0 -23 -22 z"/>
          <path d="M412 606 q14 0 12 10 q-2 8 -14 8" fill="none" stroke="var(--frame)" stroke-width="4"/>
          <ellipse cx="389" cy="634" rx="34" ry="5"/>
        </g>

        <text class="tagline" x="389" y="680" text-anchor="middle" font-size="21" textLength="217">FRESH ROASTED</text>

        <!-- bean row -->
        <rect class="bean-row" role="img" aria-label="Row of five small roasted coffee beans" x="230" y="752" width="324" height="38" rx="19" fill="var(--bean-tone)" opacity="0.55"/>

        <!-- roasted beans band -->
        <rect class="roast-band" role="img" aria-label="Silhouette of heaped roasted coffee beans" x="0" y="812" width="778" height="183" fill="var(--roast)"/>

        <text class="net-weight" x="389" y="968" text-anchor="middle" font-size="40">16 oz</text>
      </svg>
    </div>
  </div>
</body>
</html>
```